Re-work our letterhead and create a matching cover page for our FB account

We need a new letterhead to reflect our new social media branding which contains the words Wealth Retirement & Aged Care underneath the name of the company Carrow Ledger Advisers Pty Ltd. We need this logo to be able to be used as a Cover page (in .png) for our Facebook account. Colours and format to be derived from files attached.

```html
<!DOCTYPE html>
<html lang="en">
<head>
<meta charset="utf-8">
<title>Carrow Ledger Advisers – Letterhead</title>
<link href="https://fonts.googleapis.com/css2?family=Montserrat:wght@400;500;600;700&display=swap" rel="stylesheet">
<style>
  :root {
    --backdrop: #e6e6e6;
    --paper: #f1f1f1;
    --ink: #231f20;
    --body-ink: #4a4a4a;
    --gold: #c49a2c;
    --gold-soft: #e3cf9b;
    --sig-blue: #2f7fa8;
    --white: #ffffff;
  }
  * { margin: 0; padding: 0; box-sizing: border-box; }
  html, body {
    width: 1200px; height: 1079px; overflow: hidden;
    background: var(--backdrop);
    font-family: "Montserrat", sans-serif;
  }
  .letterhead {
    position: absolute; left: 230px; top: 16px;
    width: 740px; height: 1047px;
    background: var(--paper);
    overflow: hidden;
  }
  .brand { position: absolute; left: 63px; top: 38px; color: var(--ink); font-weight: 700; }
  .brand-name { font-size: 38px; line-height: 42px; letter-spacing: -0.5px; }
  .brand-suffix { font-size: 15px; line-height: 18px; letter-spacing: 0.6px; text-transform: uppercase; }
  .brand-tagline {
    position: absolute; left: 63px; top: 108px;
    font-size: 8px; font-weight: 700; letter-spacing: 3.2px; color: var(--ink);
  }
  .brand-bar {
    position: absolute; left: 63px; top: 134px; width: 205px; height: 15px;
    background: linear-gradient(90deg, var(--gold) 0%, var(--gold-soft) 55%, rgba(241,241,241,0) 100%);
  }
  .contact {
    position: absolute; left: 526px; top: 32px; width: 160px;
    font-size: 9.5px; line-height: 12px; color: var(--ink); font-weight: 500;
  }
  .contact-group { padding: 3px 0 4px; }
  .contact-rule { height: 1.5px; background: linear-gradient(90deg, var(--gold-soft), rgba(241,241,241,0)); margin: 1px 0 3px; }
  .label { color: var(--gold); font-weight: 700; }
  .phone { font-weight: 700; display: flex; align-items: center; gap: 3px; }
  .phone svg, .label svg { width: 8px; height: 8px; fill: var(--gold); }
  .salutation {
    position: absolute; left: 61px; top: 214px;
    font-size: 15px; font-weight: 500; color: var(--ink);
  }
  .letter-body {
    position: absolute; left: 63px; top: 245px; width: 615px;
    font-size: 11.5px; line-height: 16.3px; color: var(--body-ink);
    text-align: justify; hyphens: auto;
  }
  .letter-body p { margin-bottom: 16px; }
  .signature-mark {
    position: absolute; left: 46px; top: 862px; width: 250px; height: 40px;
    background: linear-gradient(90deg, rgba(47,127,168,0.18), rgba(47,127,168,0.05));
    border-radius: 4px;
  }
  .signatory { position: absolute; left: 56px; top: 906px; color: var(--ink); }
  .signatory-name { font-size: 15px; font-weight: 500; line-height: 20px; }
  .signatory-role { font-size: 11.5px; line-height: 16px; margin-left: 4px; }
  .website {
    position: absolute; left: 60px; width: 620px; top: 996px;
    font-size: 12px; font-weight: 500; color: var(--ink);
    display: flex; justify-content: space-between;
  }
  .footer-band {
    position: absolute; left: 0; bottom: 0; width: 100%; height: 27px;
    background: var(--gold); color: var(--white);
    font-size: 10.5px; line-height: 27px; text-align: center;
  }
  .footer-band strong { font-weight: 700; }
</style>
</head>
<body>
<main class="letterhead">
  <div class="brand">
    <div class="brand-name">Carrow Ledger</div>
    <div class="brand-suffix">Advisers Pty Ltd</div>
  </div>
  <div class="brand-tagline">Wealth Retirement &amp; Aged Care</div>
  <div class="brand-bar"></div>

  <aside class="contact">
    <div class="contact-group"><span class="label">ACN</span> 000 412 907</div>
    <div class="contact-rule"></div>
    <div class="contact-group">
      <div class="label"><svg viewBox="0 0 10 10"><path d="M5 1 L10 5 H8.5 V9.5 H6 V6.5 H4 V9.5 H1.5 V5 H0 Z"/></svg> Address all mail to:</div>
      <div>PO Box 418 Kelmore Vic 3521</div>
      <div>Kelmore Vic 3521</div>
    </div>
    <div class="contact-rule"></div>
    <div class="contact-group">
      <div>41 Ashford Street</div>
      <div>Kelmore Vic 3521</div>
      <div class="phone"><svg viewBox="0 0 10 10"><path d="M2 0.5 L3.8 2.6 L2.9 3.8 C3.5 5.2 4.8 6.5 6.2 7.1 L7.4 6.2 L9.5 8 L8.3 9.5 C4.5 9.3 0.7 5.5 0.5 1.7 Z"/></svg>(03) 5500 0147</div>
    </div>
    <div class="contact-rule"></div>
    <div class="contact-group">
      <div>7 Pellam St Brookvale</div>
      <div class="phone"><svg viewBox="0 0 10 10"><path d="M2 0.5 L3.8 2.6 L2.9 3.8 C3.5 5.2 4.8 6.5 6.2 7.1 L7.4 6.2 L9.5 8 L8.3 9.5 C4.5 9.3 0.7 5.5 0.5 1.7 Z"/></svg>(03) 9000 0382</div>
    </div>
  </aside>

  <p class="salutation">Dear Alan,</p>

  <section class="letter-body">
    <p>Lorem Ipsum is simply dummy text of the printing and typesetting industry. Lorem Ipsum has been the industry's standard dummy text ever since the 1500s, when an unknown printer took a galley of type and scrambled it to make a type specimen book. It has survived not only five centuries, but also the leap into electronic typesetting, remaining essentially unchanged. It was popularised in the 1960s with the release of Pressfast sheets containing Lorem Ipsum passages, and more recently with desktop publishing software like Folio Layout including versions of Lorem Ipsum.</p>
    <p>Contrary to popular belief, Lorem Ipsum is not simply random text. It has roots in a piece of classical Latin literature from 45 BC, making it over 2000 years old. Edwin Harrowgate, a Latin professor at Ashcombe College in Delmont, looked up one of the more obscure Latin words, consectetur, from a Lorem Ipsum passage, and going through the cites of the word in classical literature, discovered the undoubtable source. Lorem Ipsum comes from sections 1.10.32 and 1.10.33 of "de Finibus Bonorum et Malorum" (The Extremes of Good and Evil) by Varrus, written in 45 BC.</p>
    <p>This book is a treatise on the theory of ethics, very popular during the Renaissance. The first line of Lorem Ipsum, "Lorem ipsum dolor sit amet..", comes from<br>here are many variations of passages of Lorem Ipsum available, but the majority have suffered alteration in some form, by injected humour, or randomised words which don't look even slightly believable. If you are going to use a passage of Lorem Ipsum, you need to be sure there isn't anything embarrassing hidden in the middle of text. All the Lorem Ipsum generators on the Internet tend to repeat predefined chunks as necessary, making this the first true generator on the Internet. It uses a dictionary of over 200 Latin words, combined with a handful of model sentence structures, to generate Lorem Ipsum which looks reasonable. The generated Lorem Ipsum is therefore always free from repetition, injected humour, or non-characteristic words etc.a line in section 1.10.32.</p>
    <p>Contrary to popular belief, Lorem Ipsum is not simply random text. It has roots in a piece of classical Latin literature from 45 BC, making it over 2000 years old. Edwin Harrowgate, a Latin professor at Ashcombe College in Delmont, looked up one of the more obscure Latin words, consectetur, from a Lorem Ipsum passage, and going through the cites of the word in classical literature, discovered the undoubtable source. Lorem Ipsum comes from sections 1.10.32 and 1.10.33 of "de Finibus Bonorum et Malorum" (The Extremes of Good and Evil) by Varrus, written in 45 BC. This book is a treatise on the theory of ethics, very popular during the Renaissance. The first line of Lorem Ipsum, "Lorem ipsum dolor sit amet..", comes from a line in section 1.10.32.</p>
    <p>The standard chunk of Lorem Ipsum used since the 1500s is reproduced below for those interested. Sections 1.10.32 and 1.10.33 from "de Finibus Bonorum et Malorum" by Varrus are also reproduced in their exact original form, accompanied by English versions from the 1914 translation by H. Wendell.</p>
  </section>

  <div class="signature-mark" role="img" aria-label="Handwritten signature of Marcus Threlfall"></div>
  <div class="signatory">
    <div class="signatory-name">Marcus Threlfall</div>
    <div class="signatory-role">B. Bus., Dip. FP Authorised Representative 1048823</div>
  </div>

  <div class="website" aria-label="www.carrowledger.com.au">
    <span>w</span><span>w</span><span>w</span><span>.</span><span>c</span><span>a</span><span>r</span><span>r</span><span>o</span><span>w</span><span>l</span><span>e</span><span>d</span><span>g</span><span>e</span><span>r</span><span>.</span><span>c</span><span>o</span><span>m</span><span>.</span><span>a</span><span>u</span>
  </div>

  <footer class="footer-band">Carrow Ledger Advisers Pty Ltd is a Corporate Authorised Representative of <strong>Halden Advice Pty Ltd</strong> AFSL 000519</footer>
</main>
</body>
</html>
```